Info graphics

Create an 'info graphic' style poster to demonstrate our company employee demographics. Use the look and feel of the example infographics attached. use colours such as a dark blue background. The final design should be in word or PDF version.

Industry/Entity Type

It Company

Requirements
Must have
• Info graphic look and feel and only use the information provided and use the suggested graphics.

```html
<!DOCTYPE html>
<html lang="en">
<head>
<meta charset="utf-8">
<title>Our People Demographics</title>
<link href="https://fonts.googleapis.com/css2?family=Arimo:wght@400;700&display=swap" rel="stylesheet">
<style>
:root{
  --bg:#02628e;
  --ink:#ffffff;
  --deep:#0a86b4;
  --mid:#4ba3cc;
  --soft:#8fc1dc;
  --pale:#cfe4ef;
  --mist:#e6f1f7;
  --map:#0b80ad;
  --dark-text:#02628e;
}
*{margin:0;padding:0;box-sizing:border-box}
html,body{width:849px;height:1200px;overflow:hidden;background:var(--bg)}
body{font-family:"Arimo",Arial,sans-serif;color:var(--ink);position:relative}
.frame{position:absolute;left:9px;top:9px;right:9px;bottom:9px;border:1px dotted rgba(255,255,255,.75)}
.title{position:absolute;left:0;right:0;top:26px;text-align:center;white-space:nowrap;font-size:62px;line-height:66px;font-weight:700;letter-spacing:-.5px;transform:scaleX(.82);transform-origin:center}
.heading{position:absolute;font-size:15px;font-weight:700;letter-spacing:.3px}
.abs{position:absolute}
.body-copy{font-size:15.5px;line-height:20px}
.division-label{position:absolute;right:499px;text-align:right;font-size:10.5px;font-weight:700;line-height:14px}
.big-pct{position:absolute;font-size:35px;font-weight:700}
.bar{position:absolute;height:24px;display:flex;align-items:center;padding-left:6px;font-size:17px;font-weight:700}
.bar-note{position:absolute;font-size:15px}
.legend{position:absolute;left:258px;font-size:12.5px;display:flex;align-items:center;gap:9px}
.legend i{width:6px;height:6px;display:inline-block}
.map-area{position:absolute;left:455px;top:160px;width:345px;height:395px;border-radius:40px 60px 80px 30px;background:linear-gradient(160deg,var(--map),#0a74a0)}
.region{position:absolute;text-align:center;font-weight:700;font-size:15px;line-height:15px}
.region small{display:block;font-size:9.5px;line-height:12px}
.col-head{position:absolute;font-size:15px}
.gen-icon{position:absolute;left:462px;width:14px;height:40px;border-radius:7px 7px 3px 3px}
.gen-name{position:absolute;left:491px;font-size:10.5px}
.gen-val{position:absolute;font-size:19px;font-weight:700}
.person{position:absolute;border-radius:12px 12px 4px 4px}
.donut{position:absolute;left:40px;top:965px;overflow:visible}
.fact{position:absolute;left:459px;top:1113px;width:340px;font-size:12.5px;line-height:15px}
.fact span{display:block;font-size:9.5px}
</style>
</head>
<body>
<div class="frame"></div>
<h1 class="title">OUR PEOPLE DEMOGRAPHICS</h1>

<!-- Division sizes -->
<h2 class="heading" style="left:46px;top:137px">OUR DIVISION SIZES</h2>
<svg class="abs" style="left:0;top:170px" width="360" height="215" viewBox="0 170 360 215">
  <circle cx="147" cy="278" r="102" fill="var(--deep)"/>
  <circle cx="147" cy="301" r="79" fill="#3c96c1"/>
  <circle cx="147" cy="330" r="50" fill="var(--soft)"/>
  <circle cx="147" cy="349" r="31" fill="var(--mist)"/>
  <g stroke="rgba(255,255,255,.7)" stroke-width="1" stroke-dasharray="1 2">
    <line x1="147" y1="177" x2="350" y2="177"/>
    <line x1="147" y1="222" x2="350" y2="222"/>
    <line x1="147" y1="280" x2="350" y2="280"/>
    <line x1="147" y1="318" x2="350" y2="318"/>
  </g>
</svg>
<div class="division-label" style="top:184px">AFS<br>50.3%</div>
<div class="division-label" style="top:229px">GROUP<br>36.4%</div>
<div class="division-label" style="top:285px">CAPITAL<br>12.9%</div>
<div class="division-label" style="top:324px">SMSF<br>0.4%</div>
<p class="abs body-copy" style="left:46px;top:404px;width:292px">We have over 8,000 people working here, with 6,160 employees and 1,800 (23%) external contractors, our largest business unit is IT (in group), followed closely by Operations (in AFS).</p>

<!-- Men vs women -->
<h2 class="heading" style="left:46px;top:543px">MEN VS WOMEN</h2>
<div class="person" role="img" aria-label="Man figure" style="left:46px;top:584px;width:45px;height:114px;background:#4a9fc8"></div>
<div class="big-pct" style="left:96px;top:668px">48%</div>
<div class="person" role="img" aria-label="Woman figure" style="left:184px;top:584px;width:50px;height:114px;background:#a9d0e5"></div>
<div class="big-pct" style="left:240px;top:668px">52%</div>
<p class="abs body-copy" style="left:46px;top:730px;width:272px">40% of our leader population are female of which:</p>
<div class="bar" style="left:44px;top:796px;width:168px;background:var(--deep)">55%</div>
<div class="bar-note" style="left:218px;top:798px">at level 1-4</div>
<div class="bar" style="left:44px;top:826px;width:83px;background:#4ba3cc">37%</div>
<div class="bar-note" style="left:133px;top:828px">at level 5-6</div>
<div class="bar" style="left:44px;top:856px;width:55px;background:var(--soft)">26%</div>
<div class="bar-note" style="left:104px;top:858px">above level 6</div>

<!-- Tenure -->
<h2 class="heading" style="left:46px;top:938px">TENURE</h2>
<svg class="donut" width="200" height="200" viewBox="0 0 200 200">
  <g transform="rotate(-90 97 98)" fill="none" stroke-width="42">
    <circle cx="97" cy="98" r="71" stroke="var(--deep)" stroke-dasharray="209.7 446.1"/>
    <circle cx="97" cy="98" r="71" stroke="#4ba3cc" stroke-dasharray="98.1 446.1" stroke-dashoffset="-209.7"/>
    <circle cx="97" cy="98" r="71" stroke="var(--soft)" stroke-dasharray="75.8 446.1" stroke-dashoffset="-307.8"/>
    <circle cx="97" cy="98" r="71" stroke="var(--pale)" stroke-dasharray="62.5 446.1" stroke-dashoffset="-383.6"/>
  </g>
  <g font-family="Arimo, Arial, sans-serif" font-weight="700" font-size="17" text-anchor="middle">
    <text x="168" y="103" fill="#fff">47%</text>
    <text x="67" y="172" fill="#fff">22%</text>
    <text x="26" y="97" fill="#fff">17%</text>
    <text x="66" y="42" fill="var(--dark-text)">12%</text>
  </g>
</svg>
<div class="legend" style="top:1026px"><i style="background:var(--deep)"></i>&lt; 2 years of service</div>
<div class="legend" style="top:1053px"><i style="background:#4ba3cc"></i>2-5 years of service</div>
<div class="legend" style="top:1081px"><i style="background:var(--soft)"></i>5-10 years of service</div>
<div class="legend" style="top:1108px"><i style="background:var(--pale)"></i>&gt; 10 years of service</div>

<!-- Where we are -->
<h2 class="heading" style="left:459px;top:137px">WHERE WE ARE</h2>
<div class="map-area" role="img" aria-label="Map of Australia and New Zealand showing staff by state"></div>
<div class="region" style="left:512px;top:286px"><small>WA</small>80</div>
<div class="region" style="left:594px;top:317px"><small>SA</small>78</div>
<div class="region" style="left:704px;top:264px"><small>QLD</small>321</div>
<div class="region" style="left:708px;top:349px"><small>NSW</small>4,871</div>
<div class="region" style="left:675px;top:395px"><small>VIC</small>1,613</div>
<div class="region" style="left:702px;top:442px"><small>TAS</small>54</div>
<div class="region" style="left:758px;top:492px"><small>NZ</small>752</div>
<div class="region" style="left:462px;top:418px"><small>INTERNATIONAL</small><small style="font-weight:400;font-size:8.5px">(US, ASIA, EUROPE)</small>154</div>

<!-- Generational -->
<h2 class="heading" style="left:459px;top:583px">GENERATIONAL INSIGHTS</h2>
<div class="col-head" style="left:627px;top:621px">Employees</div>
<div class="col-head" style="left:753px;top:621px">Leaders</div>
<div class="gen-icon" role="img" aria-label="Person figure" style="top:632px;background:#1a8ab8"></div>
<div class="gen-name" style="top:660px">BABY BOOMERS</div>
<div class="gen-val" style="left:648px;top:654px">19%</div>
<div class="gen-val" style="left:762px;top:654px">25%</div>
<div class="gen-icon" role="img" aria-label="Person figure" style="top:687px;background:#5aaacf"></div>
<div class="gen-name" style="top:714px">GENERATION Y</div>
<div class="gen-val" style="left:648px;top:708px">47%</div>
<div class="gen-val" style="left:762px;top:708px">23%</div>
<div class="gen-icon" role="img" aria-label="Person figure" style="top:742px;background:#a9d0e5"></div>
<div class="gen-name" style="top:768px">GENERATION X</div>
<div class="gen-val" style="left:648px;top:761px">33%</div>
<div class="gen-val" style="left:762px;top:761px">50%</div>

<!-- Leaders -->
<h2 class="heading" style="left:459px;top:841px">OUR LEADERS</h2>
<div class="abs" role="img" aria-label="Group of leader figures" style="left:459px;top:878px;width:202px;height:62px;border-radius:8px;background:linear-gradient(90deg,#a9d0e5,#5aaacf 50%,#8fc1dc)"></div>
<div class="bar" style="left:459px;top:973px;width:184px;background:var(--deep)">29%</div>
<div class="bar-note" style="left:649px;top:976px">&lt; 2 years of service</div>
<div class="bar" style="left:459px;top:1003px;width:114px;background:#5aaacf;color:var(--dark-text)">18%</div>
<div class="bar-note" style="left:579px;top:1006px">2-5 years of service</div>
<div class="bar" style="left:459px;top:1033px;width:184px;background:var(--soft);color:var(--dark-text)">29%</div>
<div class="bar-note" style="left:649px;top:1036px">5-10 years of service</div>
<div class="bar" style="left:459px;top:1062px;width:152px;background:var(--pale);color:var(--dark-text)">24%</div>
<div class="bar-note" style="left:617px;top:1065px">&gt; 10 years of service</div>
<p class="fact"><span>INTERESTING FACT</span>56% of our leaders are level 4-5, leading over 4,300 employees (which is the majority of our employees)</p>
</body>
</html>
```